Inspirational Quotes Poster Set

Norbelle is a stylish coworking space, which has a design-oriented vintage look from the 60's with an industrial touch (www.norbelle-example.com) Norbelle Quote Poster Set of 16 posters. The poster should be typo oriented and rather simple. Reflecting a bit the clean billboard design from the sixties. Minimal / simple graphical elements

Target Market(s)

Startups and Entrepreneurs

Industry/Entity Type

Startup

Font styles to use
Sans Serif

Colors

Designer to choose colors to be used in the design.

Requirements
Must have
• Posters need to be on and very stylish

```html
<!DOCTYPE html>
<html lang="en">
<head>
<meta charset="utf-8">
<title>Norbelle Quote Poster Set – Get Shit Done</title>
<link rel="stylesheet" href="https://fonts.googleapis.com/css2?family=Arimo:wght@700&display=swap">
<style>
  :root {
    --page-bg: #ece8e3;
    --poster-blue: #1170b8;
    --bar-blue: #0b4a9e;
    --text-white: #ffffff;
  }
  html, body {
    margin: 0;
    padding: 0;
    width: 1200px;
    height: 1200px;
    overflow: hidden;
    background: var(--page-bg);
  }
  .canvas {
    width: 1200px;
    height: 1200px;
    display: flex;
    align-items: center;
    justify-content: center;
  }
  .poster {
    display: block;
    width: 830px;
    height: 1122px;
    box-shadow: 0 10px 30px rgba(0, 0, 0, 0.15);
  }
  .poster-bg { fill: var(--poster-blue); }
  .quote-line {
    font-family: "Arimo", Arial, sans-serif;
    font-weight: 700;
    font-size: 235px;
    fill: var(--text-white);
  }
  .quote-line--under { fill: var(--poster-blue); }
  .accent-bar { fill: var(--bar-blue); }
  .attribution {
    font-family: "Arimo", Arial, sans-serif;
    font-weight: 700;
    font-size: 24px;
    fill: var(--text-white);
    text-transform: uppercase;
  }
</style>
</head>
<body>
<main class="canvas">
  <svg class="poster" viewBox="0 0 880 1190" xmlns="http://www.w3.org/2000/svg" aria-label="Quote poster: get shit done, Darren Holt">
    <defs>
      <clipPath id="bar-area">
        <rect x="80" y="239" width="399" height="50"/>
        <rect x="361" y="479" width="199" height="50"/>
        <rect x="39" y="721" width="669" height="50"/>
      </clipPath>
    </defs>

    <rect class="poster-bg" x="0" y="0" width="880" height="1190"/>

    <g class="quote">
      <text class="quote-line" x="67" y="239" textLength="380" lengthAdjust="spacing">get</text>
      <text class="quote-line" x="67" y="495" textLength="456" lengthAdjust="spacing">shit</text>
      <text class="quote-line" x="67" y="734" textLength="610" lengthAdjust="spacing">done</text>
    </g>

    <g class="accent-bars">
      <rect class="accent-bar" x="80" y="239" width="399" height="50"/>
      <rect class="accent-bar" x="361" y="479" width="199" height="50"/>
      <rect class="accent-bar" x="39" y="721" width="669" height="50"/>
    </g>

    <g class="quote-knockout" clip-path="url(#bar-area)" aria-hidden="true">
      <text class="quote-line quote-line--under" x="67" y="239" textLength="380" lengthAdjust="spacing">get</text>
      <text class="quote-line quote-line--under" x="67" y="495" textLength="456" lengthAdjust="spacing">shit</text>
      <text class="quote-line quote-line--under" x="67" y="734" textLength="610" lengthAdjust="spacing">done</text>
    </g>

    <g class="attribution-block">
      <text class="attribution" x="63" y="1097">Darren Holt,</text>
      <text class="attribution" x="63" y="1129">Co-Founder &amp; Chief Executive Officer of Cratewell</text>
    </g>
  </svg>
</main>
</body>
</html>
```